Harborline Facility Systems needs a business card design with logo

need a business card and log design for a company called "Harborline Facility Systems". we improve building energy efficiency and save energy costs through building automation systems for commercial buildings such as hospitals, office buildings, universities, etc. The final design should communicate elements such as "precision", "energy efficiency", "green buildings". back side should list our service offerings

```html
<!DOCTYPE html>
<html lang="en">
<head>
<meta charset="utf-8">
<title>Harborline Facility Systems – Business Card</title>
<link href="https://fonts.googleapis.com/css2?family=Oswald:wght@500;600&family=Open+Sans:wght@400;600&display=swap" rel="stylesheet">
<style>
  :root {
    --navy: #0f2d63;
    --green: #529a1f;
    --paper: #ffffff;
    --disc: #f3f3f3;
    --backdrop: #e9e6e2;
    --text-light: #ffffff;
  }
  * { margin: 0; padding: 0; box-sizing: border-box; }
  html, body {
    width: 1200px; height: 900px; overflow: hidden;
    background: var(--backdrop);
  }
  .canvas { position: relative; width: 1200px; height: 900px; }

  .card {
    position: absolute;
    width: 610px; height: 376px;
    overflow: hidden;
    box-shadow: 0 6px 18px rgba(0,0,0,.18);
  }
  .card--front { left: 185px; top: 62px; background: var(--navy); }
  .card--back  { left: 490px; top: 487px; background: var(--navy); }

  .band-green { position: absolute; top: 0; bottom: 0; background: var(--green); }
  .card--front .band-green { left: 420px; right: 0; }
  .card--back  .band-green { left: 0; width: 193px; }

  .emblem-disc {
    position: absolute;
    width: 314px; height: 314px; border-radius: 50%;
    background: var(--disc);
    display: flex; align-items: center; justify-content: center;
  }
  .card--front .emblem-disc { left: 258px; top: 31px; }
  .card--back .emblem-disc { left: 36px; top: 31px; background: rgba(243,243,243,.88); }

  .brand-name {
    font-family: "Oswald", sans-serif;
    font-weight: 600;
    color: var(--navy);
    font-size: 30px;
    line-height: 1.12;
    text-align: center;
    text-transform: uppercase;
    letter-spacing: .5px;
  }

  .person { position: absolute; left: 32px; top: 40px; }
  .person__name {
    font-family: "Oswald", sans-serif; font-weight: 500;
    font-size: 22px; color: var(--green); letter-spacing: .3px;
    line-height: 1.1;
  }
  .person__role {
    font-family: "Open Sans", sans-serif; font-size: 17px;
    color: var(--text-light); margin-top: 2px;
  }

  .contact { position: absolute; left: 30px; top: 200px; list-style: none;
    font-family: "Open Sans", sans-serif; font-size: 16.5px; color: var(--text-light); }
  .contact li { display: flex; align-items: center; height: 22.5px; }
  .contact svg { width: 14px; height: 14px; margin-right: 7px; fill: var(--text-light); }
  .address {
    position: absolute; left: 30px; top: 297px;
    font-family: "Open Sans", sans-serif; font-size: 16.5px; line-height: 22px;
    color: var(--text-light);
  }

  .services { position: absolute; left: 379px; top: 94px;
    font-family: "Open Sans", sans-serif; color: var(--text-light); }
  .services__title { font-weight: 600; font-size: 18.5px; margin-bottom: 16px; letter-spacing: .2px; }
  .services__list { list-style: none; font-size: 16px; line-height: 25.3px; }
</style>
</head>
<body>
<main class="canvas">

  <section class="card card--front" aria-label="Business card front">
    <div class="band-green"></div>
    <div class="person">
      <p class="person__name">DANIEL WHITFORD</p>
      <p class="person__role">Managing Director</p>
    </div>
    <ul class="contact">
      <li><svg viewBox="0 0 16 16"><path d="M2 6c0-2 2-3 6-3s6 1 6 3v1h-3V5.5H5V7H2zM4 8h8l1.5 5h-11z"/></svg>044-555 018 342</li>
      <li><svg viewBox="0 0 16 16"><path d="M4.5 1h7v14h-7zM6 3v9h4V3zm1.5 10v1h1v-1z" fill-rule="evenodd"/></svg>044-555 018 342</li>
      <li><svg viewBox="0 0 16 16"><path d="M1 3.5h14v9H1zm1.5 1.2v.3L8 9l5.5-4v-.3z" fill-rule="evenodd"/></svg>hello@harborlinefs.com</li>
      <li><svg viewBox="0 0 16 16"><circle cx="8" cy="8" r="6.5"/></svg>www.harborlinefs.com</li>
    </ul>
    <p class="address">12345, Address Goes Here<br>Country Name, 123456.</p>
    <div class="emblem-disc">
      <p class="brand-name">Harborline<br>Facility Systems</p>
    </div>
  </section>

  <section class="card card--back" aria-label="Business card back">
    <div class="band-green"></div>
    <div class="emblem-disc"></div>
    <div class="services">
      <h2 class="services__title">OUR SERVICES</h2>
      <ul class="services__list">
        <li>Services Name 1</li>
        <li>Services Name 2</li>
        <li>Services Name 3</li>
        <li>Services Name 4</li>
        <li>Services Name 5</li>
        <li>Services Name 6</li>
      </ul>
    </div>
  </section>

</main>
</body>
</html>
```